Business card update

Opening a subsidiary of my company in the USA and need to update my logo.
Updates

Reason: Give more time to a good design.

I made a mistake on my briefing. It's only the business card. Thanks for alerting me on the mistake.

All the best

Leopoldo

Target Market(s)

We are an Executive Search company and our target audience are executives in large corporations.

Industry/Entity Type

Business

Requirements
Must have
• Keep the logo. In the US the company is called Declan Harrow Executive Search.

```html
<!DOCTYPE html>
<html lang="en">
<head>
<meta charset="utf-8">
<title>Declan Harrow Executive Search – Business Card</title>
<link rel="stylesheet" href="https://fonts.googleapis.com/css2?family=Questrial&display=swap">
<style>
  :root {
    --backdrop: #3f4a4d;
    --card: #ffffff;
    --teal: #4ae3b2;
    --navy: #253658;
    --ink: #1d1d1d;
    --muted: #444444;
    --alert-red: #e0201c;
  }
  * { margin: 0; padding: 0; box-sizing: border-box; }
  html, body {
    width: 1200px;
    height: 741px;
    overflow: hidden;
    background: var(--backdrop);
    font-family: "Questrial", "Century Gothic", sans-serif;
  }
  .card {
    position: absolute;
    left: 75px;
    top: 70px;
    width: 1050px;
    height: 600px;
    background: var(--card);
  }
  .brand {
    position: absolute;
    right: 40px;
    top: 70px;
    display: flex;
    align-items: center;
    gap: 18px;
  }
  .brand-dot {
    width: 26px;
    height: 26px;
    border-radius: 50%;
    background: var(--teal);
  }
  .brand-name {
    color: var(--navy);
    font-size: 44px;
    letter-spacing: 7px;
    line-height: 1;
  }
  .name-band {
    position: absolute;
    left: 0;
    top: 183px;
    width: 100%;
    height: 100px;
    background: var(--teal);
  }
  .person-name {
    position: absolute;
    left: 50px;
    bottom: 6px;
    color: #ffffff;
    font-size: 44px;
    line-height: 1;
  }
  .phone {
    position: absolute;
    left: 52px;
    top: 302px;
    display: flex;
    align-items: center;
    gap: 14px;
    color: var(--ink);
    font-size: 35px;
  }
  .phone svg { width: 28px; height: 28px; }
  .company-rule {
    position: absolute;
    left: 14px;
    right: 14px;
    top: 448px;
    display: flex;
    align-items: center;
    gap: 10px;
  }
  .company-rule .rule {
    flex: 1;
    height: 2px;
    background: var(--teal);
  }
  .company-name {
    color: var(--teal);
    font-size: 50px;
    letter-spacing: 2px;
    white-space: nowrap;
  }
  .address, .web {
    position: absolute;
    top: 520px;
    color: var(--muted);
    font-size: 27px;
    line-height: 36px;
  }
  .address { left: 50px; }
  .web { right: 38px; text-align: right; }
</style>
</head>
<body>
  <main class="card">
    <div class="brand">
      <span class="brand-dot"></span>
      <span class="brand-name">DECLAN HARROW</span>
    </div>

    <div class="name-band">
      <h1 class="person-name">Leopoldo S. Harrow</h1>
    </div>

    <p class="phone">
      <svg viewBox="0 0 24 24" aria-hidden="true">
        <path fill="var(--alert-red)" d="M6.6 10.8c1.4 2.8 3.8 5.1 6.6 6.6l2.2-2.2c.3-.3.7-.4 1-.2 1.1.4 2.3.6 3.6.6.6 0 1 .4 1 1V20c0 .6-.4 1-1 1C10.6 21 3 13.4 3 4c0-.6.4-1 1-1h3.5c.6 0 1 .4 1 1 0 1.3.2 2.5.6 3.6.1.3 0 .7-.2 1l-2.3 2.2z"/>
      </svg>
      305 555-0147
    </p>

    <div class="company-rule">
      <span class="rule"></span>
      <span class="company-name">Declan Harrow Executive Search</span>
      <span class="rule"></span>
    </div>

    <address class="address" style="font-style: normal;">
      4410 Bayview Blvd Suite 200<br>
      Harbor City FL 33100
    </address>

    <p class="web">
      www.dhexecutivesearch.com<br>
      lharrow@dhexecutivesearch.com
    </p>
  </main>
</body>
</html>
```